Creative label for amber glass candle jar.

We are a candle company. Our products are handmade by us and natural. We are looking for something minimalistic and unique. We need a label for our candle jars (amber glass with black lid). Our current label doesn't match these requirements. We would like our products to be stocked in London shop, therefore design has to be up to a high standard. Jar specification Diameter (mm) 65 Height without cap (mm) 80. We want the new design to be different from the current one. It's just a guide for wording.
We should be able adjust the label, to change scent name.
Our scents are
*Coconut & Vanilla
*Lavender
*Bergamot
*Italian Garden
*Hygge
*Eucalyptus & Peppermint
*Coffee
*Cedarwood & Juniperberry
To know more about us, visit our website www.fenwickbrae.com or instagram.com/fenwickbrae
Good luck!
Industry/Entity Type
It Company
Colors
Designer to choose colors to be used in the design.
Requirements
Must have
- * I have attached two of our logos, label design must include one of them.
- *has to mention that it's made in London
- *has to say that candle is natural/made with essential oils
- *has to have scent name and No. on it..
- Label can be vertical or horizontal, but has to be square/rectangular,.
Should not have
- Label should not be round

```html
<!DOCTYPE html>
<html lang="en">
<head>
<meta charset="utf-8">
<title>fenwickbrae — Lavender candle label</title>
<link href="https://fonts.googleapis.com/css2?family=Montserrat:wght@300;400;500;600&family=Caveat+Brush&display=swap" rel="stylesheet">
<style>
  :root {
    --page-bg: #ffffff;
    --ink: #3a3a3c;
    --ink-soft: #4a4a4c;
    --marble-light: #f4f4f4;
    --marble-mid: #dcdcdc;
    --marble-dark: #b9b9b9;
  }
  html, body {
    margin: 0;
    padding: 0;
    width: 1200px;
    height: 1200px;
    overflow: hidden;
    background: var(--page-bg);
  }
  .canvas {
    position: relative;
    width: 1200px;
    height: 1200px;
  }
  .label {
    position: absolute;
    left: 100px;
    top: 254px;
    width: 1000px;
    height: 692px;
    overflow: hidden;
  }
  .label__marble {
    position: absolute;
    inset: 0;
    background:
      radial-gradient(ellipse at 20% 80%, var(--marble-dark) 0%, transparent 45%),
      radial-gradient(ellipse at 85% 20%, var(--marble-mid) 0%, transparent 50%),
      linear-gradient(120deg, var(--marble-mid) 0%, var(--marble-light) 35%, var(--marble-light) 60%, var(--marble-mid) 100%);
  }
  .label__content {
    position: absolute;
    inset: 0;
    text-align: center;
    color: var(--ink);
    font-family: "Montserrat", sans-serif;
  }
  .brand-name {
    position: absolute;
    top: 120px;
    left: 0;
    right: 0;
    font-weight: 500;
    font-size: 62px;
    letter-spacing: 6px;
    color: var(--ink);
  }
  .scent-name {
    position: absolute;
    top: 335px;
    left: 0;
    right: 0;
    font-weight: 600;
    font-size: 37px;
    letter-spacing: 9px;
  }
  .natural-line {
    position: absolute;
    top: 418px;
    left: 0;
    right: 0;
    display: flex;
    justify-content: center;
    align-items: center;
    gap: 14px;
    font-weight: 300;
    font-size: 31px;
    letter-spacing: 7px;
  }
  .natural-line__dash {
    width: 54px;
    height: 7px;
    border-radius: 4px;
    background: var(--ink);
  }
  .tagline {
    position: absolute;
    top: 468px;
    left: 0;
    right: 0;
    font-family: "Caveat Brush", cursive;
    font-size: 64px;
    color: var(--ink-soft);
  }
  .origin {
    position: absolute;
    top: 605px;
    left: 0;
    right: 0;
    font-weight: 400;
    font-size: 33px;
    letter-spacing: 3px;
  }
</style>
</head>
<body>
  <main class="canvas">
    <section class="label">
      <div class="label__marble" role="img" aria-label="White and grey marble texture background"></div>
      <div class="label__content">
        <div class="brand-name">fenwickbrae</div>
        <div class="scent-name">LAVENDER</div>
        <div class="natural-line">
          <span class="natural-line__dash"></span>
          <span>100%NATURAL</span>
          <span class="natural-line__dash"></span>
        </div>
        <div class="tagline">Made with essential oils</div>
        <div class="origin">MADE IN LONDON</div>
      </div>
    </section>
  </main>
</body>
</html>
```